Peak Haven Fitness: Personal Training

i want to add some info onto the the flyer as listed to draw attention:
1. (visit website) www.peakhavenfitness-example.us
2.(visit online clothing store) www.peakhavenfitness.quiltmarket-example.com
3.(Note) Will work with any budget,no one gets turned away
4.Become A monthly member to reserve your spot and recieve special advantages at our private location,limited availability
5.Get one on one training with the trainer.Motivates,Listens and will help anyone reach a fitness goal.
6.Lose Weight,build muscle,Feel good about your self while making a life change,create your own body.
And not sure what color or idea i have for the background using the logo but you can play with what works.(flames,weights etc)
Clothing

```html
<!DOCTYPE html>
<html lang="en">
<head>
<meta charset="utf-8">
<title>Peak Haven Fitness – Personal Training</title>
<link rel="stylesheet" href="https://fonts.googleapis.com/css2?family=Roboto+Condensed:wght@700&display=swap">
<style>
  :root {
    --white: #ffffff;
    --black: #000000;
    --orange: #f47b20;
    --orange-band: #f7781e;
    --red-band: #ff1e00;
    --brand-red: #e0301e;
    --photo-dark: #3a3a3a;
    --photo-mid: #8a8480;
    --photo-light: #d9d6d2;
  }
  * { margin: 0; padding: 0; box-sizing: border-box; }
  html, body { width: 927px; height: 1200px; overflow: hidden; background: var(--white); }
  .flyer {
    position: relative;
    width: 927px;
    height: 1200px;
    overflow: hidden;
    font-family: "Roboto Condensed", "Arial Narrow", sans-serif;
    font-weight: 700;
    background: var(--black);
  }
  .header {
    position: absolute; left: 0; top: 0; width: 927px; height: 187px;
    background: var(--white);
  }
  .brand {
    position: absolute; left: 470px; top: 92px;
    display: flex; align-items: center; gap: 12px;
    color: var(--brand-red);
    font-size: 34px; letter-spacing: 0.5px; text-transform: uppercase;
    white-space: nowrap;
  }
  .brand-dot {
    width: 22px; height: 22px; border-radius: 50%;
    background: var(--brand-red);
  }
  .hero-photo {
    position: absolute; left: 0; top: 187px; width: 927px; height: 363px;
    background: linear-gradient(100deg, var(--photo-light) 0%, var(--photo-mid) 35%, var(--photo-dark) 70%, var(--photo-mid) 100%);
  }
  .band-orange {
    position: absolute; left: 0; top: 550px; width: 927px; height: 22px;
    background: var(--orange-band);
  }
  .band-red {
    position: absolute; left: 0; top: 572px; width: 927px; height: 19px;
    background: var(--red-band);
  }
  .links {
    position: absolute; left: 318px; top: 636px;
    list-style: none;
    color: var(--orange);
    font-size: 27px; line-height: 55px;
    white-space: nowrap;
  }
  .features {
    position: absolute; left: 297px; top: 755px;
    list-style: none;
    color: var(--white);
    font-size: 24px; line-height: 32px;
    white-space: nowrap;
  }
  .features li {
    position: relative;
    padding-left: 21px;
    margin-bottom: 30px;
  }
  .features li::before {
    content: "";
    position: absolute; left: 0; top: 11px;
    width: 11px; height: 11px; border-radius: 50%;
    background: var(--orange);
  }
</style>
</head>
<body>
  <main class="flyer">
    <header class="header">
      <div class="brand"><span class="brand-dot"></span>Peak Haven Fitness</div>
    </header>

    <div class="hero-photo" role="img" aria-label="Group fitness class doing push-ups on kettlebells in a gym"></div>
    <div class="band-orange"></div>
    <div class="band-red"></div>

    <ul class="links">
      <li>www.peakhavenfitness-example.us</li>
      <li>www.peakhavenfitness.quiltmarket-example.com</li>
    </ul>

    <ul class="features">
      <li>Will work with any budget,no one gets turned away</li>
      <li>Become A monthly member to reserve your spot and<br>recieve special advantages at our private location,<br>limited availability</li>
      <li>Get one on one training with the trainer. Motivates,<br>Listens and will help anyone reach a fitness goal.</li>
      <li>Lose Weight, build muscle, Feel good about your self<br>while making a life change, create your own body.</li>
    </ul>
  </main>
</body>
</html>
```